Meridale Dental Business Card

Please design a professional but colorful looking business card. Our new logo is attached. The card also needs the following information:
For ALL Your Dental Needs
Corbin T. Whitlow, D.D.S.
918-555-0147
20485-C North Larkspur, Oakmere, OK 74099
www.meridaledentalexample.com

```html
<!DOCTYPE html>
<html lang="en">
<head>
<meta charset="utf-8">
<title>Meridale Dental Business Card</title>
<link href="https://fonts.googleapis.com/css2?family=Quicksand:wght@500;600;700&display=swap" rel="stylesheet">
<style>
  :root {
    --page: #ecebe8;
    --slate: #626a74;
    --slate-dark: #4f5660;
    --lime: #8fd93a;
    --rose-deep: #c70f4c;
    --rose: #e8185f;
    --white: #ffffff;
    --navy: #3a3c8c;
    --sky: #29a6df;
    --sky-light: #4dbde9;
    --mist: #c9ccca;
    --ink: #2b2f36;
    --ink-soft: #3c4048;
    --brand-navy: #24337a;
  }
  html, body {
    margin: 0;
    width: 1200px;
    height: 843px;
    overflow: hidden;
    background: var(--page);
    font-family: "Quicksand", "Helvetica Neue", Arial, sans-serif;
  }
  .sheet {
    position: relative;
    width: 1200px;
    height: 843px;
    display: flex;
    align-items: center;
    justify-content: center;
    gap: 40px;
  }
  .card {
    width: 560px;
    height: 320px;
    display: block;
    box-shadow: 0 6px 18px rgba(0,0,0,0.18);
  }
  .card text { font-family: "Quicksand", "Helvetica Neue", Arial, sans-serif; }
  .tagline { font-size: 13px; font-weight: 600; }
  .doctor-name { font-size: 24px; font-weight: 600; fill: var(--white); }
  .credential { font-size: 15px; font-weight: 600; }
  .website { font-size: 13px; font-weight: 600; }
  .contact { font-size: 15px; font-weight: 600; }
  .brand-name { font-size: 20px; font-weight: 700; fill: var(--brand-navy); }
</style>
</head>
<body>
<main class="sheet">

  <!-- Rose variant -->
  <svg class="card card--rose" viewBox="0 0 560 320" xmlns="http://www.w3.org/2000/svg" role="group" aria-label="Meridale Dental business card, rose variant">
    <rect width="560" height="320" fill="var(--slate)"/>
    <polygon points="0,44 360,44 335,74 0,74" fill="var(--lime)"/>
    <polygon points="0,74 560,74 560,320 0,320" fill="var(--rose)"/>
    <polygon points="0,74 335,74 305,112 0,112" fill="var(--rose-deep)"/>
    <polygon points="335,74 560,74 560,205 250,205" fill="var(--slate)"/>
    <polygon points="560,205 560,320 470,320" fill="var(--slate-dark)"/>
    <text class="tagline" x="26" y="32" fill="var(--ink)">For ALL Your Dental Needs</text>
    <text class="doctor-name" x="26" y="100">Corbin T. Whitlow</text>
    <text class="credential" x="26" y="130" fill="var(--ink)">D.D.S.</text>
    <text class="website" x="26" y="166" fill="var(--ink)">www.meridaledentalexample.com</text>
    <rect x="336" y="129" width="24" height="24" fill="var(--white)"/>
    <text class="brand-name" x="368" y="148">Meridale Dental</text>
    <text class="contact" x="250" y="238" fill="var(--ink)">918-555-0147</text>
    <text class="contact" x="250" y="260" fill="var(--ink)">20485-C North Larkspur</text>
    <text class="contact" x="250" y="282" fill="var(--ink)">Oakmere, OK 74099</text>
  </svg>

  <!-- Sky variant -->
  <svg class="card card--sky" viewBox="0 0 560 320" xmlns="http://www.w3.org/2000/svg" role="group" aria-label="Meridale Dental business card, sky variant">
    <rect width="560" height="320" fill="var(--white)"/>
    <polygon points="0,44 360,44 335,74 0,74" fill="var(--navy)"/>
    <polygon points="0,74 335,74 305,112 0,112" fill="var(--sky)"/>
    <polygon points="0,112 305,112 272,180 0,180" fill="var(--sky-light)"/>
    <polygon points="0,180 560,180 560,320 0,320" fill="var(--mist)"/>
    <polygon points="272,180 560,180 560,212 255,212" fill="var(--white)"/>
    <text class="tagline" x="26" y="32" fill="var(--ink)">For ALL Your Dental Needs</text>
    <text class="doctor-name" x="26" y="100">Corbin T. Whitlow</text>
    <text class="credential" x="26" y="130" fill="var(--navy)">D.D.S.</text>
    <text class="website" x="26" y="166" fill="var(--ink-soft)">www.meridaledentalexample.com</text>
    <rect x="336" y="129" width="24" height="24" fill="var(--sky)"/>
    <text class="brand-name" x="368" y="148">Meridale Dental</text>
    <text class="contact" x="250" y="244" fill="var(--ink)">918-555-0147</text>
    <text class="contact" x="250" y="266" fill="var(--ink)">20485-C North Larkspur</text>
    <text class="contact" x="250" y="288" fill="var(--ink)">Oakmere, OK 74099</text>
  </svg>

</main>
</body>
</html>
```